Lebel for 500g Honey Jar

We want a design for a 500g honey bottle or Jar as shown in the attached image . All Requirement has been put in the attached brief document .
Also Logo and images have been uploaded . Feel free to play arround with the selected solor schemes .

Target Market(s)

Retail Market

Industry/Entity Type

FMCG

Colors
00AB8E
00BBA5
67D7C9
C6EFE9
E9F9F6
59FF00
82FF00
B8FF75
E3FFCB
F4FFEA
FFC000
F8CF3A
FAE287
FDF2CF
FEFAEE
F0912C
F2A743
F7CA91
FBE8D2
FDF5EE
EE7325
F08F49
F5BC92
FAE3D3
FDF4ED

Requirements
Must have
• The desing must contain the company Address, Logo , and Nutritional Facts
Nice to have
• Image of a honey Bee , see samples attahed

```html
<!DOCTYPE html>
<html lang="en">
<head>
<meta charset="utf-8">
<title>Meadowly Pure Honey – 500g Label</title>
<link href="https://fonts.googleapis.com/css2?family=Open+Sans:wght@400;600;700;800&display=swap" rel="stylesheet">
<style>
  :root {
    --backdrop: #e7e4df;
    --label-light: #f1e2b6;
    --label-mid: #e9d192;
    --label-deep: #dfbd6c;
    --brown: #3f2708;
    --ink: #1c1c1c;
    --leaf-green: #3c5a0c;
    --amber: #e89a26;
    --amber-soft: #f4c560;
  }
  * { margin: 0; padding: 0; box-sizing: border-box; }
  html, body {
    width: 760px;
    height: 1200px;
    overflow: hidden;
    background: var(--backdrop);
    font-family: "Open Sans", Arial, sans-serif;
  }
  .label {
    position: absolute;
    left: 50px;
    top: 63px;
    width: 660px;
    height: 1074px;
    border-radius: 50% 50% 56px 56px / 30% 30% 56px 56px;
    background: linear-gradient(180deg, var(--label-light) 0%, var(--label-mid) 55%, var(--label-deep) 100%);
    color: var(--ink);
    text-align: center;
  }
  .label > * {
    position: absolute;
    left: 0;
    right: 0;
  }
  .brand {
    top: 86px;
    display: flex;
    justify-content: center;
    align-items: center;
    gap: 12px;
    font-weight: 700;
    font-size: 60px;
    letter-spacing: -1px;
    color: var(--ink);
    line-height: 1;
  }
  .brand-dot {
    width: 16px;
    height: 16px;
    border-radius: 50%;
    background: var(--ink);
  }
  .product-kicker {
    top: 204px;
    font-weight: 700;
    font-size: 74px;
    line-height: 1;
    color: var(--brown);
  }
  .product-name {
    top: 283px;
    font-weight: 800;
    font-size: 134px;
    line-height: 1;
    letter-spacing: 4px;
    color: var(--brown);
  }
  .purity-claim {
    top: 406px;
    font-weight: 700;
    font-size: 44px;
    line-height: 1;
    letter-spacing: 1px;
    color: var(--leaf-green);
  }
  .free-from {
    top: 461px;
    font-weight: 600;
    font-size: 21px;
    line-height: 1;
    color: var(--ink);
  }
  .distributor {
    top: 515px;
    left: 164px;
    right: auto;
    width: 333px;
    height: 72px;
    border: 2px solid var(--ink);
    display: flex;
    flex-direction: column;
    justify-content: center;
    gap: 4px;
    font-size: 17px;
    line-height: 1.15;
  }
  .distributor strong { font-weight: 700; }
  .hero-art {
    top: 607px;
    left: 150px;
    right: auto;
    width: 360px;
    height: 396px;
    border-radius: 46% 46% 40% 40%;
    background: radial-gradient(ellipse at 50% 60%, var(--amber-soft) 0%, var(--amber) 45%, rgba(232,154,38,0) 72%);
  }
  .net-weight {
    top: 1028px;
    font-weight: 700;
    font-size: 22px;
    line-height: 1;
    color: var(--ink);
  }
</style>
</head>
<body>
  <main class="label">
    <div class="brand"><span class="brand-name">meadowly</span><span class="brand-dot"></span></div>
    <h2 class="product-kicker">PURE</h2>
    <h1 class="product-name">HONEY</h1>
    <p class="purity-claim">100% PURE &amp; NATURAL</p>
    <p class="free-from">Zero additive - zero colouring . zero preservative</p>
    <div class="distributor">
      <span>Packed &amp; Distributed by</span>
      <strong>Fieldcrest Farms Limited</strong>
    </div>
    <div class="hero-art" role="img" aria-label="Illustration of a honey jar with cloth lid, honeycomb, daisies, a honey dipper and two flying bees"></div>
    <p class="net-weight">Net WT: 500g</p>
  </main>
</body>
</html>
```